Business Card Design

We would like a business card that utilizes our current logo and keeps with the same feel - elegant and organic. Our farm isn't about mass production, it's about excellence, education, beautiful events and flowers - people, culture, and community.

Target Market(s)

Patrons to our farm who are interested in weddings, events, or our flowers and vegetables.

Contact Information for Business Card

Name, address, cell email (Danielle Hoskins, 2716 Wrenfield Rd, Elmdale, CO 80927, cell 30.412.6638, email danielle@wrenfieldacres.com)

```html
<!DOCTYPE html>
<html lang="en">
<head>
<meta charset="utf-8">
<title>Wrenfield Acres — Business Card</title>
<link href="https://fonts.googleapis.com/css2?family=Poppins:wght@300;400;500;600&display=swap" rel="stylesheet">
<style>
  :root {
    --canvas: #e7e8ea;
    --card: #ffffff;
    --card-back: #f3f3f3;
    --sage: #7a8c7b;
    --sage-panel: #778a7a;
    --sage-deep: #627a65;
    --clay: #a47c55;
    --leaf-faint: #e9e7e1;
    --white: #ffffff;
  }
  * { margin: 0; padding: 0; box-sizing: border-box; }
  html, body { width: 1200px; height: 1200px; overflow: hidden; }
  body {
    background: var(--canvas);
    font-family: "Poppins", sans-serif;
    position: relative;
  }
  .card {
    position: absolute;
    left: 276px;
    width: 647px;
    height: 388px;
    overflow: hidden;
    box-shadow: 5px 5px 6px rgba(60, 60, 70, 0.35);
  }
  .card--front { top: 155px; background: var(--card); }
  .card--back  { top: 640px; background: var(--card-back); }
  .card__shapes { position: absolute; inset: 0; width: 100%; height: 100%; }

  .brand {
    position: absolute;
    transform: translate(-50%, -50%);
    color: var(--sage);
    font-size: 27px;
    font-weight: 400;
    letter-spacing: 1px;
    white-space: nowrap;
  }
  .card--front .brand { left: 326px; top: 193px; }
  .card--back .brand  { left: 494px; top: 196px; }

  .website {
    position: absolute;
    display: flex;
    align-items: center;
    gap: 9px;
    color: var(--clay);
    font-size: 12.5px;
    letter-spacing: 1.6px;
  }
  .card--front .website { left: 246px; top: 328px; }
  .card--back .website  { left: 430px; top: 329px; }
  .icon-dot {
    width: 18px; height: 18px; border-radius: 50%;
    display: flex; align-items: center; justify-content: center;
    flex: none;
  }
  .website .icon-dot { background: var(--sage); }

  .person {
    position: absolute;
    left: 41px;
    top: 112px;
    color: var(--white);
  }
  .person__name {
    font-size: 27px;
    font-weight: 400;
    letter-spacing: 1px;
    line-height: 1;
    text-transform: uppercase;
  }
  .person__name strong { font-weight: 600; }
  .person__role {
    margin-top: 10px;
    font-size: 16.5px;
    font-weight: 300;
    letter-spacing: 0.8px;
    display: flex;
    align-items: center;
  }
  .person__rule {
    width: 65px; height: 2px;
    background: var(--sage-deep);
    margin-left: 19px;
    margin-top: 4px;
  }

  .contacts {
    position: absolute;
    left: 41px;
    top: 262px;
    list-style: none;
    color: var(--white);
    font-size: 12.3px;
    font-weight: 300;
    letter-spacing: 0.8px;
  }
  .contacts li { display: flex; align-items: center; gap: 13px; height: 18px; white-space: nowrap; }
  .contacts li + li { margin-top: 15px; }
  .contacts li:last-child { margin-top: 14px; }
  .contacts .icon-dot { background: var(--white); }
</style>
</head>
<body>

<section class="card card--front" aria-label="Card front">
  <svg class="card__shapes" viewBox="0 0 1042 625" preserveAspectRatio="none" aria-hidden="true">
    <path fill="var(--sage)" d="M0,0 H258 C215,80 150,130 80,140 C45,146 15,158 0,166 Z"/>
    <path fill="var(--clay)" d="M0,0 H220 C180,70 120,110 60,125 C30,133 10,145 0,150 Z"/>
    <path fill="var(--sage)" d="M785,625 C810,570 850,520 950,495 C990,485 1020,475 1042,460 V625 Z"/>
    <path fill="var(--clay)" d="M822,625 C845,575 890,535 980,515 C1010,508 1030,500 1042,490 V625 Z"/>
  </svg>
  <svg class="card__shapes" viewBox="0 0 1042 625" preserveAspectRatio="none" role="img" aria-label="Illustrated leafy sprig on a stem, upper right">
    <rect x="760" y="80" width="240" height="150" rx="75" fill="var(--sage)" transform="rotate(28 880 155)"/>
  </svg>
  <svg class="card__shapes" viewBox="0 0 1042 625" preserveAspectRatio="none" role="img" aria-label="Illustrated leafy sprig on a stem, lower left">
    <rect x="60" y="395" width="240" height="150" rx="75" fill="var(--sage)" transform="rotate(28 180 470)"/>
  </svg>

  <div class="brand">Wrenfield Acres</div>

  <div class="website">
    <span class="icon-dot"><svg width="11" height="11" viewBox="0 0 12 12" fill="none" stroke="#fff" stroke-width="1"><circle cx="6" cy="6" r="5"/><ellipse cx="6" cy="6" rx="2.2" ry="5"/><path d="M1 6h10M1.8 3.5h8.4M1.8 8.5h8.4"/></svg></span>
    <span>www.website.com</span>
  </div>
</section>

<section class="card card--back" aria-label="Card back">
  <svg class="card__shapes" viewBox="0 0 1042 625" preserveAspectRatio="none" aria-hidden="true">
    <defs>
      <clipPath id="panel-clip">
        <path d="M0,0 H528 C470,70 480,160 520,260 C570,380 600,470 590,540 C580,590 565,610 557,625 H0 Z"/>
      </clipPath>
    </defs>
    <path fill="var(--white)" d="M0,0 H565 C520,50 500,150 540,250 C600,390 640,480 625,560 C615,600 600,615 592,625 H0 Z"/>
    <g clip-path="url(#panel-clip)">
      <rect width="1042" height="625" fill="var(--sage-panel)"/>
      <circle cx="530" cy="40" r="100" fill="var(--sage-deep)"/>
      <path fill="var(--sage-deep)" d="M468,625 C478,580 515,560 555,520 C585,490 600,460 610,440 V625 Z"/>
    </g>
    <path fill="none" stroke="var(--clay)" stroke-width="5" d="M565,0 C520,50 505,150 545,250 C600,390 640,480 625,560 C615,600 600,615 592,625"/>
  </svg>
  <svg class="card__shapes" viewBox="0 0 1042 625" preserveAspectRatio="none" role="img" aria-label="Faint leafy sprig decoration behind the contact details">
    <rect x="245" y="330" width="260" height="140" rx="70" fill="var(--sage-deep)" opacity="0.35" transform="rotate(25 375 400)"/>
  </svg>
  <svg class="card__shapes" viewBox="0 0 1042 625" preserveAspectRatio="none" role="img" aria-label="Faint leafy sprig decoration, upper right">
    <rect x="770" y="90" width="260" height="150" rx="75" fill="var(--leaf-faint)" transform="rotate(30 900 165)"/>
  </svg>

  <div class="person">
    <h1 class="person__name"><strong>Danielle</strong> Hoskins</h1>
    <p class="person__role">Designation Here <span class="person__rule"></span></p>
  </div>

  <ul class="contacts">
    <li>
      <span class="icon-dot"><svg width="10" height="10" viewBox="0 0 24 24" fill="var(--sage-panel)"><path d="M6.6 10.8a15.2 15.2 0 0 0 6.6 6.6l2.2-2.2a1 1 0 0 1 1-.25 11.4 11.4 0 0 0 3.6.57 1 1 0 0 1 1 1V20a1 1 0 0 1-1 1A17 17 0 0 1 3 4a1 1 0 0 1 1-1h3.5a1 1 0 0 1 1 1c0 1.25.2 2.450.57 3.57a1 1 0 0 1-.25 1z"/></svg></span>
      <span>30.412.6638</span>
    </li>
    <li>
      <span class="icon-dot"><svg width="10" height="10" viewBox="0 0 24 24" fill="var(--sage-panel)"><path d="M3 9l9-6 9 6v11H3z"/><path d="M3 9l9 6 9-6" fill="none" stroke="#fff" stroke-width="2"/></svg></span>
      <span>danielle@wrenfieldacres.com</span>
    </li>
    <li>
      <span class="icon-dot"><svg width="10" height="11" viewBox="0 0 24 24" fill="var(--sage-panel)"><path d="M12 2a7 7 0 0 0-7 7c0 5 7 13 7 13s7-8 7-13a7 7 0 0 0-7-7zm0 9.5A2.5 2.5 0 1 1 12 6.5a2.5 2.5 0 0 1 0 5z"/></svg></span>
      <span>2716 Wrenfield Rd, Elmdale, CO 80927</span>
    </li>
  </ul>

  <div class="brand">Wrenfield Acres</div>

  <div class="website">
    <span class="icon-dot"><svg width="11" height="11" viewBox="0 0 12 12" fill="none" stroke="#fff" stroke-width="1"><circle cx="6" cy="6" r="5"/><ellipse cx="6" cy="6" rx="2.2" ry="5"/><path d="M1 6h10M1.8 3.5h8.4M1.8 8.5h8.4"/></svg></span>
    <span>www.website.com</span>
  </div>
</section>

</body>
</html>
```